Website design: professional but personally
Needs:
Our visitors are mostly people that look for a IT or technical jobs, but our customers are also visiting our website.
Core values are: personally, professional, ambition, growth, personal development
Terms that we think of are:
Professional, but personal (we ware no trading company, but we do have internation customers)
People
IT (jobs)
Engineering (jobs)

```html
<!DOCTYPE html>
<html lang="nl">
<head>
<meta charset="utf-8">
<title>Velwerk – IT &amp; Engineering jobs</title>
<link href="https://fonts.googleapis.com/css2?family=PT+Sans:wght@400;700&family=Open+Sans:wght@400;600;700&display=swap" rel="stylesheet">
<style>
:root{
  --green:#8cc63f;
  --green-dark:#76ad2c;
  --ink:#2f2f2f;
  --grey:#8a8a8a;
  --light:#f3f3f3;
  --card:#f6f6f6;
  --nav-active:#3b3b3b;
  --white:#ffffff;
}
*{margin:0;padding:0;box-sizing:border-box}
html,body{width:1200px;height:3686px;overflow:hidden}
body{position:relative;background:var(--white);font-family:"PT Sans",sans-serif;color:var(--ink)}
.abs{position:absolute}
section,header,footer{position:absolute;left:0;width:1200px}

/* header */
.site-header{top:0;height:64px;background:var(--green)}
.brand{left:96px;top:14px;font:700 32px/36px "PT Sans",sans-serif;color:var(--white);letter-spacing:2px}
.nav a{position:absolute;top:0;height:64px;line-height:66px;color:var(--white);font:700 14px/66px "Open Sans",sans-serif;text-decoration:none;text-align:center}
.nav a.active{background:var(--nav-active)}

/* hero */
.hero{top:64px;height:634px}
.hero-photo{position:absolute;inset:0;background:linear-gradient(100deg,#d9d3cc 0%,#b9aea3 30%,#8f8a86 55%,#6e6f73 75%,#9aa0a5 100%)}
.hero h1{left:596px;top:230px;font:700 64px/70px "PT Sans",sans-serif;color:var(--white);letter-spacing:-1px}
.hero p{left:596px;top:302px;width:500px;font:400 17px/22px "Open Sans",sans-serif;color:var(--white);text-align:justify}
.btn{background:var(--green);color:var(--white);font-family:"Open Sans",sans-serif;font-weight:700;text-align:center;text-decoration:none;display:block}
.hero .btn{left:764px;top:380px;width:116px;height:48px;font-size:17px;line-height:48px}
.dots{display:flex;gap:10px}
.dots span{width:13px;height:13px;border-radius:50%;background:var(--white)}
.dots span.on{background:var(--green)}
.hero .dots{left:550px;top:600px}

/* jobs */
.jobs{top:698px;height:322px;background:linear-gradient(#f7f7f7,#ececec)}
.jobs-photo{left:278px;top:50px;width:644px;height:272px;background:radial-gradient(ellipse at 50% 45%,#e4d3c4 0%,#c9bdb2 25%,#eeeeee 60%,rgba(236,236,236,0) 75%)}
.job-tile{top:54px;width:172px;height:172px;background:var(--green);color:var(--white);text-align:center;display:flex;flex-direction:column;justify-content:center}
.job-tile strong{font:700 22px/24px "PT Sans",sans-serif}
.job-tile small{font:700 10px/14px "Open Sans",sans-serif}

/* services */
.services{top:1020px;height:666px}
.section-title{width:1200px;text-align:center;font:700 32px/36px "PT Sans",sans-serif;color:var(--green)}
.service-card{top:122px;width:310px;height:398px;background:var(--card);text-align:center}
.service-card svg{position:absolute;left:105px;top:16px}
.service-card h3{position:absolute;top:124px;width:100%;font:700 26px/27px "PT Sans",sans-serif;color:var(--ink)}
.service-card h3 em{font-style:normal;color:var(--green);display:block}
.service-card hr{position:absolute;left:20px;top:188px;width:270px;border:0;border-top:2px solid #dcdcdc}
.service-card p{position:absolute;left:22px;top:212px;width:266px;font:400 13.5px/26px "Open Sans",sans-serif;color:var(--grey);text-align:justify}
.service-card .btn{position:absolute;left:104px;top:380px;width:104px;height:30px;font-size:10px;line-height:30px}

/* success factors */
.factors{top:1686px;height:378px}
.factors-photo{position:absolute;inset:0;background:linear-gradient(90deg,#3a3c3f 0%,#1e2023 30%,#2a2d31 60%,#17191b 100%)}
.factors h2{top:42px;width:1200px;text-align:center;font:700 34px/40px "PT Sans",sans-serif;color:var(--green)}
.factors h3{top:122px;width:1200px;text-align:center;font:700 23px/28px "Open Sans",sans-serif;color:var(--white)}
.factors p{left:256px;top:160px;width:688px;text-align:center;font:400 18.5px/30px "Open Sans",sans-serif;color:var(--white)}

/* why */
.why{top:2064px;height:460px}
.why h2{top:50px;width:1200px;text-align:center;font:700 27px/28px "PT Sans",sans-serif;color:var(--green)}
.why h2 span{display:block;color:var(--ink)}
.why-item{top:160px;width:270px;height:270px;border-radius:50%;background:var(--white);box-shadow:0 0 10px rgba(0,0,0,.08);text-align:center}
.why-item svg{position:absolute;left:105px;top:40px}
.why-item p{position:absolute;top:126px;width:100%;font:400 13px/21px "Open Sans",sans-serif;color:var(--ink)}
.why-item a{position:absolute;top:182px;width:100%;left:0;font:700 11.5px/16px "Open Sans",sans-serif;color:var(--green);text-decoration:underline}

/* testimonial */
.testimonial{top:2524px;height:466px}
.testimonial-photo{position:absolute;inset:0;background:linear-gradient(#2b2d30 0%,#3c3f42 40%,#2a2c2e 100%)}
.avatar{left:490px;top:62px;width:164px;height:164px;border-radius:50%;border:6px solid var(--green);background:linear-gradient(#e9e6e3,#b9b2ab)}
.testimonial blockquote{left:244px;top:266px;width:712px;text-align:center;font:400 17px/24px "Open Sans",sans-serif;color:var(--white)}
.quote-mark{font:700 40px/40px "PT Sans",sans-serif;color:var(--white)}
.testimonial cite{top:340px;width:1200px;text-align:center;font-style:normal;color:var(--white)}
.testimonial cite strong{display:block;font:700 19px/24px "Open Sans",sans-serif}
.testimonial cite span{font:400 14px/20px "Open Sans",sans-serif}
.testimonial .dots{left:530px;top:420px}

/* team */
.team{top:2990px;height:410px}
.team-map{left:30px;top:40px;width:640px;height:330px;background:radial-gradient(ellipse at 50% 50%,#dcdcdc 0%,#efefef 60%,#fafafa 100%)}
.team-copy{left:700px;top:120px;width:380px;text-align:center}
.team-copy h2{font:700 44px/42px "PT Sans",sans-serif;color:var(--green)}
.team-copy .lead{font:700 14px/18px "Open Sans",sans-serif;color:var(--green)}
.team-copy .sub{font:700 15px/20px "Open Sans",sans-serif;color:var(--ink)}

/* footer */
.site-footer{top:3400px;height:286px;background:var(--green)}
.footer-col{top:50px}
.footer-col h4{font:700 15px/20px "Open Sans",sans-serif;color:var(--ink);margin-bottom:30px;text-transform:uppercase}
.footer-col li{list-style:none;font:400 15px/30px "Open Sans",sans-serif;color:var(--white);display:flex;align-items:center;gap:22px}
.footer-col li i{width:14px;height:14px;border-radius:50%;background:var(--ink);display:inline-block}
</style>
</head>
<body>

<header class="site-header">
  <div class="abs brand">Velwerk</div>
  <nav class="nav">
    <a href="#" class="active" style="left:388px;width:100px">HOME</a>
    <a href="#" style="left:506px;width:190px">ONZE DIENSTVERLENING</a>
    <a href="#" style="left:730px;width:110px">VACATURES</a>
    <a href="#" style="left:866px;width:92px">OVER ONS</a>
    <a href="#" style="left:960px;width:140px">OUR CUSTOMERS</a>
  </nav>
</header>

<section class="hero">
  <div class="hero-photo" role="img" aria-label="Photo of a smiling man working on a laptop by a large window"></div>
  <h1 class="abs">Business Solutions</h1>
  <p class="abs">Optimale ondersteuning van uw primaire bedrijfsprocessen? Wij ontzorgen support afdelingen op operationeel gebied: van individueel niveau tot het compleet outsourcen.</p>
  <a href="#" class="abs btn">Read More</a>
  <div class="abs dots"><span class="on"></span><span></span><span></span><span></span></div>
</section>

<section class="jobs">
  <div class="abs jobs-photo" role="img" aria-label="Photo of a smiling businessman in white shirt and tie with open hands"></div>
  <div class="abs job-tile" style="left:100px"><strong>IT</strong><small>(TECHNICAL) JOBS</small></div>
  <div class="abs job-tile" style="left:928px"><strong>ENGINEERING</strong><small>(TECHNICAL) JOBS</small></div>
</section>

<section class="services">
  <h2 class="abs section-title" style="top:70px">ONZE DIENSTEN</h2>

  <article class="abs service-card" style="left:100px">
    <svg width="100" height="100" viewBox="0 0 100 100" aria-hidden="true">
      <path d="M4 36 L22 22 L34 40 L16 56 Z" fill="#8cc63f"/>
      <path d="M96 36 L78 22 L66 40 L84 56 Z" fill="#8cc63f"/>
      <path d="M30 36 L48 28 L60 30 L74 44 L54 72 Q48 78 42 72 L24 54 Z" fill="#8cc63f"/>
      <path d="M46 34 L38 44 Q44 48 52 40" fill="none" stroke="#f6f6f6" stroke-width="3"/>
    </svg>
    <h3><em>BUSINESS</em>SOLUTIONS</h3>
    <hr>
    <p>Optimale ondersteuning van uw primaire bedrijfsprocessen? Wij ontzorgen support afdelingen op operationeel gebied: van individueel niveau tot het compleet outsourcen.</p>
    <a href="#" class="btn">Read More</a>
  </article>

  <article class="abs service-card" style="left:442px">
    <svg width="100" height="100" viewBox="0 0 100 100" aria-hidden="true">
      <circle cx="22" cy="30" r="8" fill="#444"/><rect x="12" y="40" width="20" height="44" rx="4" fill="#444"/>
      <circle cx="78" cy="30" r="8" fill="#444"/><rect x="68" y="40" width="20" height="44" rx="4" fill="#444"/>
      <circle cx="38" cy="28" r="8" fill="#555"/><rect x="28" y="38" width="20" height="48" rx="4" fill="#555"/>
      <circle cx="62" cy="28" r="8" fill="#555"/><rect x="52" y="38" width="20" height="48" rx="4" fill="#555"/>
      <circle cx="50" cy="16" r="10" fill="#8cc63f"/><rect x="38" y="28" width="24" height="60" rx="5" fill="#8cc63f"/>
    </svg>
    <h3><em>TALENT</em>SOLUTIONS</h3>
    <hr>
    <p>Talent Solutions richt zich volledig op de sourcing en het ontwikkelen van hoogopgeleid IT en technisch talent. Onze trainees borgen de instroom van kennis binnen ..</p>
    <a href="#" class="btn">Read More</a>
  </article>

  <article class="abs service-card" style="left:788px">
    <svg width="100" height="100" viewBox="0 0 100 100" aria-hidden="true">
      <path d="M50 4 C28 4 18 20 18 34 C18 56 50 90 50 90 C50 90 82 56 82 34 C82 20 72 4 50 4 Z" fill="#8cc63f"/>
      <circle cx="50" cy="34" r="22" fill="#f6f6f6"/>
      <circle cx="50" cy="24" r="5" fill="#8cc63f"/>
      <rect x="44" y="31" width="12" height="20" rx="3" fill="#8cc63f"/>
    </svg>
    <h3><em>INTERIM</em>SOLUTIONS</h3>
    <hr>
    <p>Wilt u op korte termijn IT professionals inhuren? Vanuit ons netwerk beschikken wij over de juiste, gekwalificeerde en gedreven medewerker(s) om bij uw bedrijf het verschil ..</p>
    <a href="#" class="btn">Read More</a>
  </article>
</section>

<section class="factors">
  <div class="factors-photo" role="img" aria-label="Photo of a technician with a laptop in a server room"></div>
  <h2 class="abs">ONZE SUCCESFACTOREN</h2>
  <h3 class="abs">1000+ IT EN TECHNISCHE PROFESSIONALS IN VASTE DIENST</h3>
  <p class="abs">Als enige organisatie in Nederland heeft Velwerk ruim 1000 jonge ICT en technische medewerkers voor u klaar staan. Velwerk is een betrouwbare installatiepartner voor de groot zakelijke markt.</p>
  <svg class="abs" style="left:62px;top:160px" width="36" height="76" viewBox="0 0 36 76" aria-label="Vorige"><path d="M32 4 L6 38 L32 72" fill="none" stroke="#8cc63f" stroke-width="6"/></svg>
  <svg class="abs" style="left:1102px;top:160px" width="36" height="76" viewBox="0 0 36 76" aria-label="Volgende"><path d="M4 4 L30 38 L4 72" fill="none" stroke="#8cc63f" stroke-width="6"/></svg>
</section>

<section class="why">
  <h2 class="abs">SUCCESVOL OMDAT<span>WE HET ANDERS DOEN</span></h2>

  <div class="abs why-item" style="left:104px">
    <svg width="60" height="60" viewBox="0 0 60 60" aria-hidden="true"><circle cx="24" cy="24" r="16" fill="none" stroke="#8cc63f" stroke-width="2.5"/><path d="M36 36 L54 54" stroke="#8cc63f" stroke-width="3"/></svg>
    <p>IJzersterk in de werving<br>van young professionals</p>
    <a href="#">Know More</a>
  </div>
  <div class="abs why-item" style="left:360px">
    <svg width="60" height="60" viewBox="0 0 60 60" aria-hidden="true"><path d="M30 4 L37 22 L56 23 L41 35 L46 54 L30 43 L14 54 L19 35 L4 23 L23 22 Z" fill="none" stroke="#8cc63f" stroke-width="2.5" stroke-linejoin="round"/></svg>
    <p>IJzersterk in de werving<br>van young professionals</p>
    <a href="#">Know More</a>
  </div>
  <div class="abs why-item" style="left:620px">
    <svg width="60" height="60" viewBox="0 0 60 60" aria-hidden="true"><path d="M48 22 A20 20 0 0 0 12 22" fill="none" stroke="#8cc63f" stroke-width="2.5"/><path d="M42 16 L49 23 L52 14" fill="none" stroke="#8cc63f" stroke-width="2.5"/><path d="M12 38 A20 20 0 0 0 48 38" fill="none" stroke="#8cc63f" stroke-width="2.5"/><path d="M18 44 L11 37 L8 46" fill="none" stroke="#8cc63f" stroke-width="2.5"/></svg>
    <p>IJzersterk in de werving<br>van young professionals</p>
    <a href="#">Know More</a>
  </div>
  <div class="abs why-item" style="left:878px">
    <svg width="60" height="60" viewBox="0 0 60 60" aria-hidden="true"><path d="M12 4 H38 L48 14 V56 H12 Z" fill="none" stroke="#8cc63f" stroke-width="2.5" stroke-linejoin="round"/><path d="M38 4 V14 H48" fill="none" stroke="#8cc63f" stroke-width="2.5"/><text x="30" y="44" text-anchor="middle" font-family="Open Sans, sans-serif" font-size="22" fill="#8cc63f">€</text></svg>
    <p>IJzersterk in de werving<br>van young professionals</p>
    <a href="#">Know More</a>
  </div>
</section>

<section class="testimonial">
  <div class="testimonial-photo" role="img" aria-label="Photo of a city skyline under a dark sky"></div>
  <div class="abs avatar" role="img" aria-label="Portrait photo of the managing director"></div>
  <span class="abs quote-mark" style="left:204px;top:248px">“</span>
  <blockquote class="abs">Optimale ondersteuning van uw primaire bedrijfsprocessen? Wij ontzorgen support afdelingen op operationeel gebied: van individueel niveau tot het compleet outsourcen.</blockquote>
  <span class="abs quote-mark" style="left:946px;top:302px">”</span>
  <cite class="abs"><strong>Martin</strong><span>Managing Director, Norvia</span></cite>
  <div class="abs dots"><span class="on"></span><span></span><span></span><span></span></div>
</section>

<section class="team">
  <div class="abs team-map" role="img" aria-label="Dotted world map marking office cities"></div>
  <div class="abs team-copy">
    <h2>ONZE<br>MEDEWERKERS</h2>
    <p class="lead">ZIJN DOOR HEEL NEDERLAND INZETBAAR.</p>
    <p class="sub">WE HEBBEN EEN LANDELIJK<br>DEKKEND PERSONEELSBESTAND.</p>
  </div>
</section>

<footer class="site-footer">
  <div class="abs footer-col" style="left:108px">
    <h4>Adresgegevens</h4>
    <ul><li>Velwerk B.V.</li><li>Lindenlaan 120B</li><li>3511 KL Utrecht</li><li>0850 123 456</li><li>Privacy Policy</li></ul>
  </div>
  <div class="abs footer-col" style="left:362px">
    <h4>Voor opdrachtgevers</h4>
    <ul><li>Klanten over Velwerk</li><li>Login urenregistratiesysteem</li><li>Nieuws</li></ul>
  </div>
  <div class="abs footer-col" style="left:650px">
    <h4>Voor werkzoekenden</h4>
    <ul><li>IT Traineeship</li><li>Technisch Traineeship</li><li>Werken en leren in de ICT</li><li>Sollicitatietips</li></ul>
  </div>
  <div class="abs footer-col" style="left:936px">
    <h4>Connect</h4>
    <ul><li><i></i>Chirp</li><li><i></i>Facepage</li><li><i></i>Linkwise</li><li><i></i>Tubecast</li></ul>
  </div>
</footer>

</body>
</html>
```